Etiketten auf Kühlschrank Wasserfilter Velmiro
Zielgruppe
Wasserfilter Velmiro
Aufgabenstellung
Ich brauche eine neue Etikette auf Kühlschrank Wasserfilter Velmiro. die Massse der Etikette muss gleiche wie die alte Etikett.

```html
<!DOCTYPE html>
<html lang="en">
<head>
<meta charset="utf-8">
<title>Velmiro Refrigerator Water Filter Label</title>
<link href="https://fonts.googleapis.com/css2?family=Montserrat:wght@400;800;900&family=Poppins:wght@400;500;600&display=swap" rel="stylesheet">
<style>
  :root {
    --navy: #1f3380;
    --navy-deep: #18296b;
    --navy-mid: #2a4796;
    --sky-light: #eef7fd;
    --sky-mid: #bfe0f6;
    --splash: #3f7fcc;
    --page: #ffffff;
  }
  * { box-sizing: border-box; margin: 0; padding: 0; }
  html, body { width: 1200px; height: 982px; overflow: hidden; background: var(--page); }
  .canvas { position: relative; width: 1200px; height: 982px; }
  .label {
    position: absolute; left: 130px; top: 21px; width: 940px; height: 940px;
    overflow: hidden; color: var(--navy);
    font-family: "Poppins", sans-serif;
  }
  .label__backdrop {
    position: absolute; inset: 0;
    background:
      radial-gradient(ellipse 62% 60% at 50% 50%, var(--sky-light) 0%, #e2f1fb 55%, var(--sky-mid) 80%, var(--splash) 100%);
  }
  .label__content { position: absolute; inset: 0; text-align: center; }
  .title { font-family: "Montserrat", sans-serif; line-height: 1; letter-spacing: -1px; }
  .title__main { position: absolute; left: 0; right: 0; top: 85px; font-size: 84px; font-weight: 900; color: var(--navy-deep); }
  .title__sub { position: absolute; left: 0; right: 0; top: 159px; font-size: 90px; font-weight: 400; color: var(--navy); }
  .replacement { position: absolute; left: 0; right: 0; top: 258px; font-size: 27px; font-weight: 500; }
  .specs { position: absolute; left: 74px; top: 311px; width: 793px; border-collapse: collapse; text-align: left; }
  .specs th {
    height: 70px; padding: 0 16px; font-size: 27px; font-weight: 600; color: #fff;
    background: linear-gradient(90deg, var(--navy-deep), var(--navy-mid));
  }
  .specs th + th, .specs td + td { border-left: 2px solid #fff; }
  .specs td + td { border-left-color: var(--navy); }
  .specs td { height: 50px; padding: 0 16px; font-size: 23px; font-weight: 500; border-bottom: 2px solid var(--navy); }
  .specs th:first-child, .specs td:first-child { width: 372px; }
  .marks { position: absolute; left: 145px; top: 600px; width: 644px; display: flex; justify-content: space-between; align-items: flex-start; }
  .mark { width: 130px; display: flex; flex-direction: column; align-items: center; font-size: 15px; font-weight: 600; font-family: "Montserrat", sans-serif; }
  .mark svg { width: 120px; height: 120px; }
  .disclaimer { position: absolute; left: 60px; right: 60px; top: 746px; font-size: 17px; font-weight: 500; line-height: 1.35; }
  .install { position: absolute; left: 0; right: 0; top: 805px; display: flex; justify-content: center; align-items: center; gap: 50px; font-size: 40px; }
  .install__arrow { position: relative; width: 286px; height: 64px; }
  .install__arrow svg { position: absolute; inset: 0; }
  .install__arrow span { position: absolute; left: 0; width: 255px; top: 14px; font-size: 23px; color: #fff; text-align: center; }
</style>
</head>
<body>
<div class="canvas">
  <section class="label">
    <div class="label__backdrop" role="img" aria-label="Blue water splash illustration framing a pale blue centre"></div>
    <div class="label__content">
      <h1 class="title">
        <span class="title__main">REFRIGERATOR</span>
        <span class="title__sub">WATER FILTER</span>
      </h1>
      <p class="replacement">Replacement for:&nbsp; Korvane® filter KV47-31158R</p>
      <table class="specs">
        <thead><tr><th>Application Guidelines</th><th>Water Supply Parameters</th></tr></thead>
        <tbody>
          <tr><td>Flow rate:</td><td>0.55GPM / 2.1LPM</td></tr>
          <tr><td>Operating Temperature:</td><td>34°F - 100°F / 1°C - 38°C</td></tr>
          <tr><td>Operating Pressure:</td><td>30PSI - 120 PSI / 207kPa - 827 kPa</td></tr>
          <tr><td>Capacity:</td><td>300 Gallons or 1135 liters</td></tr>
        </tbody>
      </table>
      <div class="marks">
        <div class="mark">
          <svg viewBox="0 0 120 120" aria-label="Replace every 6 months">
            <path d="M20 60 A40 40 0 1 1 60 100" fill="none" stroke="var(--navy)" stroke-width="3"/>
            <path d="M60 100 l-8 -6 M60 100 l-8 6" stroke="var(--navy)" stroke-width="3"/>
            <text x="60" y="78" text-anchor="middle" font-family="Montserrat, sans-serif" font-weight="800" font-size="54" fill="var(--navy)">6</text>
          </svg>
        </div>
        <div class="mark">
          <svg viewBox="0 0 120 120" aria-label="Recycling code 5">
            <polygon points="60,14 106,94 14,94" fill="none" stroke="var(--navy)" stroke-width="12" stroke-linejoin="round"/>
            <text x="60" y="80" text-anchor="middle" font-family="Montserrat, sans-serif" font-weight="800" font-size="26" fill="var(--navy)">5</text>
          </svg>
          <span>PP</span>
        </div>
        <div class="mark">
          <svg viewBox="0 0 120 120" aria-label="Food contact safe">
            <path d="M20 14 h52 v34 q0 26 -26 26 q-26 0 -26 -26 z M46 74 v30 M30 104 h32" fill="none" stroke="var(--navy)" stroke-width="5"/>
            <path d="M84 14 v30 q0 10 8 10 q8 0 8 -10 v-30 M92 54 v52" fill="none" stroke="var(--navy)" stroke-width="5"/>
          </svg>
          <span>EC 1935/2004</span>
        </div>
        <div class="mark">
          <svg viewBox="0 0 120 120" aria-label="Quality certification badge">
            <circle cx="60" cy="60" r="52" fill="none" stroke="var(--navy)" stroke-width="4"/>
            <circle cx="60" cy="60" r="30" fill="none" stroke="var(--navy)" stroke-width="3"/>
          </svg>
        </div>
      </div>
      <p class="disclaimer">*All trademarks remain the property of their respective holder(s) and are used for compatibility information only. AClaims of compatibility verified through manufacture testing.</p>
      <div class="install">
        <span>Lock</span>
        <div class="install__arrow">
          <svg viewBox="0 0 286 64"><polygon points="0,16 250,16 250,0 286,32 250,64 250,48 0,48" fill="var(--navy)"/></svg>
          <span>Install</span>
        </div>
        <span>Start</span>
      </div>
    </div>
  </section>
</div>
</body>
</html>
```